Business Card Design Project

Financial planning, Insurance and Real estate - Financial Services company

Contact Information for Business Card

Looking for something simple in design -
Tolverin Equity LLC
Tolverin Wealth Managment

```html
<!DOCTYPE html>
<html lang="en">
<head>
<meta charset="UTF-8">
<title>Tolverin Wealth Management – Business Card</title>
<link href="https://fonts.googleapis.com/css2?family=Roboto+Condensed:wght@400;700&display=swap" rel="stylesheet">
<style>
  :root {
    --backdrop: #2a2a2a;
    --card: #f4f4f4;
    --brand-blue: #0a7cc1;
    --ink: #4a4a4a;
    --rule: #3a9fd6;
  }
  * { margin: 0; padding: 0; box-sizing: border-box; }
  html, body {
    width: 1200px;
    height: 960px;
    overflow: hidden;
    background: var(--backdrop);
  }
  .canvas {
    position: relative;
    width: 1200px;
    height: 960px;
  }
  .card {
    position: absolute;
    left: 429px;
    top: 180px;
    width: 342px;
    height: 599px;
    background: var(--card);
    font-family: "Roboto Condensed", "Arial Narrow", sans-serif;
    text-align: center;
  }
  .card > * {
    position: absolute;
    left: 0;
    width: 100%;
  }
  .brand-name {
    top: 218px;
    font-size: 15px;
    font-weight: 700;
    color: var(--brand-blue);
    letter-spacing: 0;
  }
  .holder-name {
    top: 306px;
    font-size: 29px;
    font-weight: 700;
    color: var(--brand-blue);
    line-height: 1;
  }
  .holder-title {
    top: 340px;
    font-size: 14px;
    font-weight: 700;
    color: var(--ink);
  }
  .divider {
    left: 71px;
    width: 200px;
    height: 1px;
    background: linear-gradient(to right, transparent, var(--rule) 30%, var(--rule) 70%, transparent);
  }
  .divider--upper { top: 377px; }
  .divider--lower { top: 472px; }
  .address, .contact {
    font-size: 15px;
    font-weight: 700;
    color: var(--ink);
    line-height: 20px;
    font-style: normal;
  }
  .address { top: 395px; }
  .contact { top: 490px; }
</style>
</head>
<body>
<div class="canvas">
  <section class="card">
    <p class="brand-name">Tolverin Wealth Management</p>

    <h1 class="holder-name">ELIAS MARLOW</h1>
    <p class="holder-title">CEO/FOUNDER</p>

    <div class="divider divider--upper"></div>

    <address class="address">
      Tolverin Equity LLC<br>
      4213 Harbor Ridge Road<br>
      Kenai, Alaska 99611
    </address>

    <div class="divider divider--lower"></div>

    <p class="contact">
      (P) 907 555 0184<br>
      elias@tolverin.com<br>
      www.tolverin.com
    </p>
  </section>
</div>
</body>
</html>
```